Independent Midwife for a positive birth experience needs a vibrant, and elegant business card/logo

I need a business card design with a logo. The logo I would like to be able to use on my website (www.midwifeorlaith.com) next to my name.
Therefore the design of the card and logo should suit the colours and design of the website. The title of the website and company is "Orlaith Denby Marsworth, Midwife" but I'd like to have the business card title to be "Orlaith Denby Marsworth - Independent Midwife" in bold letters, same script font as in my website.

I provide gold standard midwifery services, one-to-one tailored care, continuity of care throughout the entire pregnancy (antenatal care), the birth and after the birth (postnatal care), home birth, water birth, breast-feeding support, and birth preparation workshops. I also am certified and offer complementary therapies: pregnancy reflexology, rebozo techniques for optimal baby positioning.

The design should incorporate similar colours and style as the website and the "Orlaith Denby Marsworth - Independent Midwife" on the card should include the same font as in the title of the website, however, in bold. The front of the card should have a logo, title and contact information (phone number 071592604, email orlaith.marsworth@quillpost.com, website address www.midwifeorlaith.com).
The back of the card to include the services I offer.

The logo: use of colour purple (varying shades), should communicate communicate warmth, kindness, compassion. It should convey that I'm a midwife who believes in fostering a trusting relationship with my clients and to provide them with a positive pregnancy and birth experience.

Target Market(s)

Pregnant women or women who are looking to book a private midwife for better birth experience and outcome

Industry/Entity Type

Baby

Contact Information for Business Card

Name and Title on front side together with contact details
The reverse side should have services/packages offered

Font styles to use
Script
Other font styles liked:
• similar script as in my website for name and title, and easy to read font for the rest of the words

Colors
b768aa
a54599
d2a4cc
ffffff

Requirements
Must have
• same font as title of website, but slightly bolder.
• similar design, colours, patterns as in website.
• Also include a gold accent colour somewhere in the design please.
Nice to have
• perhaps a logo of pregnant belly in profile or newborn baby icon

```html
<!DOCTYPE html>
<html lang="en">
<head>
<meta charset="utf-8">
<title>Orlaith Denby Marsworth - Independent Midwife - Business Card</title>
<link rel="stylesheet" href="https://fonts.googleapis.com/css2?family=Cookie&family=Lato:wght@400;700&display=swap">
<style>
  :root {
    --stage: #000000;
    --plum: #a54599;
    --plum-soft: #b768aa;
    --lilac: #d2a4cc;
    --white: #ffffff;
    --ink: #2b2b2b;
    --rule: #d4d4d4;
    --rule-mid: #bdbdbd;
  }
  * { box-sizing: border-box; margin: 0; padding: 0; }
  html, body {
    width: 1200px; height: 900px; overflow: hidden;
    background: var(--stage);
    font-family: "Lato", Arial, sans-serif;
  }
  .stage { position: relative; width: 1200px; height: 900px; }

  /* Front */
  .card-front {
    position: absolute; left: 99px; top: 78px;
    width: 590px; height: 336px; background: var(--white);
  }
  .title-band {
    position: absolute; left: 21px; top: 21px;
    width: 547px; height: 116px; background: var(--plum);
  }
  .script-title {
    font-family: "Cookie", "Brush Script MT", cursive;
    color: var(--white); font-weight: 400;
    white-space: nowrap;
    text-shadow: 0.4px 0 0 var(--white), -0.4px 0 0 var(--white);
  }
  .title-band .script-title {
    position: absolute; left: 26px; top: 44px; font-size: 31px; line-height: 1;
  }
  .logo-mark {
    position: absolute; background: var(--white);
    border-radius: 0 45% 45% 0 / 0 30% 30% 0;
  }
  .title-band .logo-mark { left: 487px; top: 16px; width: 22px; height: 88px; }
  .rule { position: absolute; height: 1px; background: var(--rule); }
  .rule-top { left: 21px; top: 149px; width: 547px; }
  .rule-bottom { left: 21px; top: 314px; width: 547px; }
  .divider { position: absolute; left: 295px; top: 166px; width: 1px; height: 133px; background: var(--rule-mid); }

  .contact-list { position: absolute; left: 21px; top: 174px; list-style: none; }
  .contact-item {
    display: flex; align-items: center; height: 24px; margin-bottom: 13px;
    font-size: 13px; color: var(--ink);
  }
  .contact-icon {
    width: 24px; height: 24px; border-radius: 50%;
    background: var(--plum); margin-right: 5px;
    display: flex; align-items: center; justify-content: center; flex: none;
  }
  .contact-icon svg { width: 12px; height: 12px; }

  .holder { position: absolute; left: 296px; top: 196px; width: 275px; text-align: center; }
  .holder-name { font-size: 27px; color: var(--ink); letter-spacing: 0.3px; line-height: 1; }
  .holder-name .accent { color: var(--plum); }
  .holder-role { margin-top: 18px; font-size: 11px; color: var(--ink); letter-spacing: 0.3px; }

  /* Back */
  .card-back {
    position: absolute; left: 441px; top: 474px;
    width: 591px; height: 337px; overflow: hidden;
    background: linear-gradient(160deg, #a7489b 0%, var(--plum) 60%, #9f4194 100%);
  }
  .backdrop-figure {
    position: absolute; left: 515px; top: 0; width: 120px; height: 337px;
    background: linear-gradient(90deg, rgba(210,164,204,0.35), rgba(210,164,204,0.2));
    border-radius: 60px 0 0 90px;
  }
  .services {
    position: absolute; top: 112px; list-style: none;
    font-size: 12px; line-height: 18.8px; color: var(--white);
  }
  .services-left { right: 347px; text-align: right; }
  .services-right { left: 322px; width: 170px; }
  .card-back .logo-mark { left: 267px; top: 105px; width: 29px; height: 107px; }
  .rule-light { position: absolute; left: 20px; width: 550px; height: 1px; background: rgba(255,255,255,0.85); }
  .rule-light-top { top: 233px; }
  .rule-light-bottom { top: 295px; }
  .card-back .script-title {
    position: absolute; left: 0; width: 591px; top: 249px;
    text-align: center; font-size: 31px; line-height: 1;
  }
</style>
</head>
<body>
<main class="stage">

  <section class="card-front" aria-label="Business card front">
    <div class="title-band">
      <h1 class="script-title">Orlaith Denby Marsworth - Independent Midwife</h1>
      <div class="logo-mark" role="img" aria-label="Logo: pregnant woman profile silhouette"></div>
    </div>
    <div class="rule rule-top"></div>

    <ul class="contact-list">
      <li class="contact-item">
        <span class="contact-icon">
          <svg viewBox="0 0 24 24"><path fill="#fff" d="M3 9c0-3 4-5 9-5s9 2 9 5l-1 2-4-1V8c-2-.7-6-.7-8 0v2l-4 1zM6 13h12l1 7H5z"/></svg>
        </span>
        071592604
      </li>
      <li class="contact-item">
        <span class="contact-icon">
          <svg viewBox="0 0 24 24"><rect x="2" y="5" width="20" height="14" fill="none" stroke="#fff" stroke-width="2"/><path d="M2 5l10 8 10-8" fill="none" stroke="#fff" stroke-width="2"/></svg>
        </span>
        orlaith.marsworth@quillpost.com
      </li>
      <li class="contact-item">
        <span class="contact-icon">
          <svg viewBox="0 0 24 24"><path d="M10 14l4-4M9 11l-3 3a3 3 0 004 4l3-3M15 13l3-3a3 3 0 00-4-4l-3 3" fill="none" stroke="#fff" stroke-width="2.2" stroke-linecap="round"/></svg>
        </span>
        www.midwifeorlaith.com
      </li>
    </ul>

    <div class="divider"></div>

    <div class="holder">
      <p class="holder-name"><span class="accent">YOUR</span> NAME</p>
      <p class="holder-role">DESIGNATION</p>
    </div>

    <div class="rule rule-bottom"></div>
  </section>

  <section class="card-back" aria-label="Business card back">
    <div class="backdrop-figure" role="img" aria-label="Faint large pregnant woman silhouette decoration"></div>

    <ul class="services services-left">
      <li>One-to-one tailored care</li>
      <li>Antenatal care</li>
      <li>Postnatal care</li>
      <li>Home birth</li>
      <li>Water birth</li>
    </ul>
    <div class="logo-mark" role="img" aria-label="Logo: pregnant woman profile silhouette"></div>
    <ul class="services services-right">
      <li>Breast-feeding support</li>
      <li>Birth preparation workshops</li>
      <li>Pregnancy reflexology</li>
      <li>Rebozo techniques for optimal baby positioning.</li>
    </ul>

    <div class="rule-light rule-light-top"></div>
    <h2 class="script-title">Orlaith Denby Marsworth - Independent Midwife</h2>
    <div class="rule-light rule-light-bottom"></div>
  </section>

</main>
</body>
</html>
```